Website Design for an Exciting, Fun & Premium Cannabis Company

Website will be designed and implemented for Wordpress with the ability to connect Leafroute Bazaar.
Looking to build trust with website visitors with engaging, exciting & informative content that will drive business to local dispensaries within the state of Oklahoma.
The website will embody excitement, fun, enthusiasm and make the visitor identify with the content and emphasize with a fun life they can have or believe they can have by using our products & will allow for super charged SEO and other digital marketing and advertising strategies and tactics used to increase discovery, awareness, and conversion.

Target Market(s)

Male/Female Ages 21-45

Coding

Coded - Design and coding required

Number of Pages Required

5+ page

Font styles to use
Sans Serif

Requirements
Must have
• Please see attached document for this information
Nice to have
Should not have

```html
<!DOCTYPE html>
<html lang="en">
<head>
<meta charset="utf-8">
<title>Vivra THC</title>
<link href="https://fonts.googleapis.com/css2?family=Playfair+Display:wght@700;800&family=Poppins:wght@400;500;600&display=swap" rel="stylesheet">
<style>
:root{
  --cyan:#1aa7d4;
  --green:#5cbf3a;
  --pale-green:#cfe9c2;
  --ink:#1a1a1a;
  --muted:#666;
  --gray-band:#efefef;
  --white:#fff;
  --serif:'Playfair Display',Georgia,serif;
  --sans:'Poppins',Arial,sans-serif;
}
*{box-sizing:border-box;margin:0;padding:0}
html,body{width:1200px;height:4616px;overflow:hidden}
body{position:relative;font-family:var(--sans);color:var(--ink);background:var(--white);font-size:13px;line-height:1.6}
section,header,footer,div,nav{position:absolute}
.inline{position:static}
.btn{display:inline-block;font-family:var(--sans);font-size:11px;font-weight:600;letter-spacing:.5px;padding:9px 20px;text-transform:uppercase}
.btn-cyan{background:var(--cyan);color:var(--white)}
.btn-outline{border:1px solid var(--white);color:var(--white)}
.section-title{position:absolute;font-family:var(--serif);font-weight:800;font-size:40px;text-align:center;width:1200px;left:0}
.ph{border-radius:2px}

.promo-bar{top:0;left:0;width:1200px;height:28px;background:var(--cyan);color:var(--white);font-size:11px;text-align:center;line-height:28px}
.site-header{top:28px;left:0;width:1200px;height:92px;background:var(--white)}
.brand{left:80px;top:26px;font-weight:600;font-size:26px;color:var(--cyan);display:flex;align-items:center;gap:8px;line-height:40px}
.brand .dot{position:static;width:14px;height:14px;border-radius:50%;background:var(--green)}
.nav{left:378px;top:34px;display:flex;gap:34px;font-size:12px;font-weight:600;text-transform:uppercase;line-height:24px}
.nav-icons{left:1010px;top:36px;display:flex;gap:18px}

.hero{top:120px;left:0;width:1200px;height:540px;background:linear-gradient(100deg,#c9d4c1 0%,#8aa36e 35%,#587a3e 65%,#3e5a2c 100%)}
.hero-person{left:80px;top:130px;width:180px;height:410px;background:linear-gradient(#8a6a4a,#4a3a2a)}
.hero-product{left:300px;top:250px;width:280px;height:250px;background:linear-gradient(135deg,#e83fa0,#f6e24a,#3bb3e8,#5a2d8c)}
.hero-copy{left:640px;top:230px;color:var(--white)}
.hero-copy h1{font-family:var(--serif);font-size:38px;line-height:1.2;font-weight:800}
.hero-copy p{width:390px;font-size:12px;margin:12px 0 22px}
.hero-copy .btn{margin-right:14px}
.dots{left:560px;top:505px;display:flex;gap:8px}
.dots span{width:8px;height:8px;border-radius:50%;background:rgba(255,255,255,.6)}
.dots span:first-child{background:var(--white)}

.sellers-title{top:742px}
.product-card{top:820px;width:232px;height:290px;background:var(--white);box-shadow:0 2px 14px rgba(0,0,0,.12);text-align:center}
.product-card .ph{left:41px;top:20px;width:150px;height:150px;background:linear-gradient(135deg,#f04a9b,#f7dd3b,#29a9e1,#222)}
.product-card .info{left:0;top:186px;width:100%}
.stars{color:#f4b400;font-size:14px;letter-spacing:2px}
.product-card .name{font-size:12px;font-weight:500}
.product-card .price{font-size:12px;color:var(--muted)}
.card-actions{top:1126px;left:362px;display:flex;gap:10px}
.card-actions span{font-size:10px;font-weight:600;color:var(--white);padding:7px 12px}
.arrow{width:28px;height:28px;border-radius:50%;background:var(--green);color:var(--white);text-align:center;line-height:28px;font-weight:600}

.difference{top:1320px;left:0;width:1200px;height:440px;background:linear-gradient(90deg,#050505 0%,#121212 50%,#2b2b2b 100%)}
.difference .copy{left:100px;top:90px;color:var(--white);width:430px}
.difference h2{font-family:var(--serif);font-size:40px;line-height:1.15;font-weight:800}
.difference p{font-size:12px;margin:14px 0 22px;color:#ddd}
.difference .visual{left:660px;top:60px;width:440px;height:330px;background:linear-gradient(135deg,#3c5a2e,#1b1b1b 60%,#e74a9b)}

.testimonial-title{top:1838px}
.testimonial{top:1920px;width:450px;height:250px;border:3px solid var(--pale-green);background:var(--white);padding:24px 30px}
.testimonial .quote{position:static;font-family:var(--serif);font-size:48px;color:var(--green);line-height:.8}
.testimonial p{font-size:12px;color:var(--muted);margin:10px 0 18px}
.testimonial .foot{position:static;display:flex;justify-content:space-between;font-weight:600;font-size:12px}

.gray-band{top:2400px;left:0;width:1200px;height:700px;background:var(--gray-band)}
.subscribe{top:2268px;left:148px;width:900px;height:272px;background:linear-gradient(90deg,#e2399b 0%,#ef6b4a 35%,#f3d33a 60%,#6cc43a 100%)}
.subscribe .ph{left:36px;top:36px;width:190px;height:200px;background:linear-gradient(135deg,#3bb3e8,#f04a9b,#f7dd3b)}
.subscribe .copy{left:310px;top:44px;color:var(--white);width:540px}
.subscribe h2{font-family:var(--serif);font-size:38px;line-height:1.15;font-weight:800}
.subscribe p{font-size:11px;margin:12px 0 18px}

.cbd{top:2620px;left:0;width:1200px;height:460px}
.cbd .copy{left:124px;top:0;width:450px}
.cbd h2{font-family:var(--serif);font-size:40px;font-weight:800}
.cbd p{font-size:12px;color:#333;margin:8px 0 14px}
.cbd .flower{left:0;top:300px;width:90px;height:90px;border-radius:50%;background:radial-gradient(#f6e7e4,#b9a59c)}
.cbd .photo-a{left:690px;top:60px;width:190px;height:160px;background:linear-gradient(135deg,#3a2a55,#d54a8f,#f4d24a)}
.cbd .photo-b{left:770px;top:210px;width:150px;height:150px;background:linear-gradient(#c8c8c8,#5b4f40)}
.cbd .photo-c{left:920px;top:110px;width:120px;height:150px;background:linear-gradient(135deg,#e74a9b,#f5dd3c,#2fa8e0)}
.cbd .leaf{left:960px;top:-20px;width:140px;height:130px;border-radius:50%;background:radial-gradient(#5fa640,#2f6a22)}
.cbd .photo-d{left:680px;top:270px;width:90px;height:110px;background:linear-gradient(#eae3d6,#b6a68a)}

.blog-title{top:3078px}
.blog-card{top:3152px;width:312px;height:460px;background:var(--white);box-shadow:0 2px 14px rgba(0,0,0,.1)}
.blog-card .ph{left:0;top:0;width:312px;height:200px}
.blog-card .body{left:24px;top:224px;width:264px}
.blog-card h3{font-size:19px;font-weight:600;line-height:1.35}
.blog-card p{font-size:13px;color:var(--muted);margin:12px 0 22px;line-height:1.65}
.read-more{display:inline-block;border:1px solid #bbb;font-size:12px;padding:8px 18px}
.view-all{position:absolute;top:3722px;left:522px}

.partners{top:3842px;left:0;width:1200px;display:flex;justify-content:space-around;padding:0 80px}
.partners span{position:static;display:block;height:30px;background:#9a9a9a;border-radius:3px}
.chat{top:3880px;left:1150px;width:44px;height:44px;border-radius:50%;background:var(--cyan)}

.touch{top:3940px;left:0;width:1200px;height:220px;background:linear-gradient(90deg,#1c3318,#2e5226,#1c3318)}
.touch h2{position:absolute;left:0;top:46px;width:1200px;text-align:center;font-family:var(--serif);font-size:40px;font-weight:800;color:var(--white)}
.touch .form{left:316px;top:134px;display:flex}
.touch .field{width:420px;height:44px;border:1px solid var(--white);background:rgba(255,255,255,.1);color:var(--white);font-size:12px;padding:12px 18px}
.touch .submit{width:150px;height:44px;background:var(--cyan);color:var(--white);font-size:12px;font-weight:600;text-align:center;line-height:44px}

.site-footer{top:4160px;left:0;width:1200px;height:456px}
.col{top:28px}
.col h4{font-size:14px;font-weight:600;margin-bottom:8px}
.col ul{list-style:none;font-size:11px;color:#444;line-height:1.7}
.links-2{display:grid;grid-template-columns:100px 100px}
.foot-brand{left:946px;top:30px;font-size:24px;font-weight:600;color:var(--cyan)}
.socials{left:958px;top:80px;display:flex;gap:8px}
.socials span{width:24px;height:24px;border-radius:50%;border:1px solid #999}
.copyright{left:100px;top:140px;width:1000px;border-top:1px solid #ddd;padding-top:10px;font-size:11px;color:#555}
.cards{left:880px;top:148px;display:flex;gap:6px}
.cards span{width:34px;height:22px;border-radius:3px;background:#c9c9c9}
.disclaimer{left:100px;top:200px;width:1000px}
.disclaimer h4{font-size:16px;font-weight:600;margin-bottom:6px}
.disclaimer p{font-size:10px;color:#555;line-height:1.6}
</style>
</head>
<body>

<div class="promo-bar">Free Delivery On Orders Over $50</div>

<header class="site-header">
  <div class="brand"><span class="dot"></span>Vivra THC</div>
  <nav class="nav"><span>Home</span><span>Products</span><span>Order Tracking</span><span>About</span><span>Review</span><span>FAQ</span></nav>
  <div class="nav-icons">
    <svg width="18" height="18" viewBox="0 0 18 18" fill="none" stroke="#222" stroke-width="1.6"><circle cx="9" cy="6" r="3.5"/><path d="M2 17c1-4 4-5 7-5s6 1 7 5"/></svg>
    <svg width="18" height="18" viewBox="0 0 18 18" fill="none" stroke="#222" stroke-width="1.6"><path d="M3 5h12l-1 11H4z"/><path d="M6 5a3 3 0 0 1 6 0"/></svg>
    <svg width="18" height="18" viewBox="0 0 18 18" fill="none" stroke="#222" stroke-width="1.6"><circle cx="7.5" cy="7.5" r="5"/><path d="M11 11l5 5"/></svg>
  </div>
</header>

<section class="hero">
  <div class="hero-person ph" role="img" aria-label="Woman in a hat sitting on a hillside overlooking green fields"></div>
  <div class="hero-product ph" role="img" aria-label="Colourful product box and bottle"></div>
  <div class="hero-copy">
    <h1>Highest Quality Product<br>Vivra THC</h1>
    <p>Lorem ipsum dolor sit amet, consectetur adipiscing elit, sed do eiusmod tempor incididunt ut labore et dolore magna aliqua.</p>
    <span class="btn btn-cyan">Learn More</span><span class="btn btn-outline">Shop Now</span>
  </div>
  <div class="dots"><span class="inline"></span><span class="inline"></span><span class="inline"></span></div>
</section>

<h2 class="section-title sellers-title">Shop Our Best Sellers</h2>
<div class="arrow" style="left:36px;top:950px">&lsaquo;</div>
<div class="arrow" style="left:1136px;top:950px">&rsaquo;</div>
<div class="product-card" style="left:92px"><div class="ph" role="img" aria-label="Product box"></div><div class="info"><div class="stars inline">★★★★★</div><div class="name inline">Product Name Oil 6000mg</div><div class="price inline">$100.00</div></div></div>
<div class="product-card" style="left:352px"><div class="ph" role="img" aria-label="Product bottle"></div><div class="info"><div class="stars inline">★★★★★</div><div class="name inline">Product Name Oil 6000mg</div><div class="price inline">$100.00</div></div></div>
<div class="card-actions"><span style="background:var(--cyan)">ADD TO CART</span><span style="background:var(--green)">BUY NOW</span></div>
<div class="product-card" style="left:612px"><div class="ph" role="img" aria-label="Product box and bottle"></div><div class="info"><div class="stars inline">★★★★★</div><div class="name inline">Product Name Oil 6000mg</div><div class="price inline">$100.00</div></div></div>
<div class="product-card" style="left:872px"><div class="ph" role="img" aria-label="Product box and bottle"></div><div class="info"><div class="stars inline">★★★★★</div><div class="name inline">Product Name Oil 6000mg</div><div class="price inline">$100.00</div></div></div>

<section class="difference">
  <div class="copy">
    <h2>The Vivra_THC<br>Cbd Difference</h2>
    <p>Lorem ipsum dolor sit amet, consectetur adipiscing elit, duimolempor incididunt ut labore et dolore magna aliqua, a risus ultrices gravida. Risus commodo viverra maecenas accumsan lacus vel facilisis.<br>Lorem ipsum dolor sit amet, consectetur adipiscing elit.</p>
    <span class="btn btn-cyan">Shop Now</span>
  </div>
  <div class="visual ph" role="img" aria-label="Potted plant beside product box and bottle on a dark table"></div>
</section>

<h2 class="section-title testimonial-title">Our Testimonial</h2>
<div class="arrow" style="left:36px;top:2030px">&lsaquo;</div>
<div class="arrow" style="left:1136px;top:2030px">&rsaquo;</div>
<div class="testimonial" style="left:100px"><div class="quote">&ldquo;</div><p>Lorem ipsum dolor sit amet, consectetur adipiscing elit, sedd do eiusmod tempor incididunt ut labore et dolore magna aliqua. Quis ipsum suspendisse ultrices gravida. Risus co viverra maecenas accumsan lacus vel facilisis.</p><div class="foot"><span>– Jan Y.</span><span class="stars">★★★★★</span></div></div>
<div class="testimonial" style="left:650px"><div class="quote">&ldquo;</div><p>Lorem ipsum dolor sit amet, consectetur adipiscing elit, sedd do eiusmod tempor incididunt ut labore et dolore magna aliqua. Quis ipsum suspendisse ultrices gravida. Risus co viverra maecenas accumsan lacus vel facilisis.</p><div class="foot"><span>– Jan Y.</span><span class="stars">★★★★★</span></div></div>

<div class="gray-band"></div>
<section class="subscribe">
  <div class="ph" role="img" aria-label="Product box and bottle with a 30% off badge"></div>
  <div class="copy">
    <h2>Subscribe + Save 30% off<br>Every Order.</h2>
    <p>Join our membership subscription and save 30% between right to your door save 30% off your order when you subscribe.</p>
    <span class="btn btn-outline">Subscribe Now</span>
  </div>
</section>

<section class="cbd">
  <div class="copy">
    <h2>CBD101</h2>
    <p>Lorem ipsum dolor sit amet, consectetur adipiscing elit, duimolempor incididunt ut labore et dolore magna aliqua, a risus ultrices gravida. Risus commodo viverra maecenas accumsan.</p>
    <p>Lorem ipsum dolor sit amet, consectetur adipiscing elit, duimolempor incididunt ut labore et dolore magna aliqua, a risus ultrices gravida. Risus commodo viverra maecenas accumsan.</p>
    <span class="btn btn-cyan">Shop Now</span>
  </div>
  <div class="flower ph" role="img" aria-label="Pale rose flower"></div>
  <div class="leaf ph" role="img" aria-label="Green cannabis leaf"></div>
  <div class="photo-a ph" role="img" aria-label="Product box on a purple surface"></div>
  <div class="photo-c ph" role="img" aria-label="Colourful product box"></div>
  <div class="photo-b ph" role="img" aria-label="Person standing in a field at dusk"></div>
  <div class="photo-d ph" role="img" aria-label="Small flowers in a vase"></div>
</section>

<h2 class="section-title blog-title">Latest Blog Post</h2>
<div class="blog-card" style="left:100px"><div class="ph" role="img" aria-label="Cannabis plant close-up" style="background:linear-gradient(135deg,#5b7a3a,#2f4a1e)"></div><div class="body"><h3>Lorem ipsum amet, consectetur adipiscing elit, sed do</h3><p>Lorem ipsum dolor sit amet, consectetur adipiscing elit, sed do eiusmod tempor incididunt ut labore et dolore magna aliqua.</p><span class="read-more">Read more &rarr;</span></div></div>
<div class="blog-card" style="left:444px"><div class="ph" role="img" aria-label="Gloved hands trimming a cannabis plant" style="background:linear-gradient(135deg,#e9efe6,#7fa35a)"></div><div class="body"><h3>Lorem ipsum amet, consectetur adipiscing elit, sed do</h3><p>Lorem ipsum dolor sit amet, consectetur adipiscing elit, sed do eiusmod tempor incididunt ut labore et dolore magna aliqua.</p><span class="read-more">Read more &rarr;</span></div></div>
<div class="blog-card" style="left:788px"><div class="ph" role="img" aria-label="Grower inspecting plants in a greenhouse" style="background:linear-gradient(135deg,#8a7a55,#3d5428)"></div><div class="body"><h3>Lorem ipsum amet, consectetur adipiscing elit, sed do</h3><p>Lorem ipsum dolor sit amet, consectetur adipiscing elit, sed do eiusmod tempor incididunt ut labore et dolore magna aliqua.</p><span class="read-more">Read more &rarr;</span></div></div>
<span class="btn btn-cyan view-all">View All Articles</span>

<div class="partners" aria-label="Partner badges"><span style="width:90px"></span><span style="width:120px"></span><span style="width:100px"></span><span style="width:60px"></span><span style="width:110px"></span></div>
<div class="chat"><svg width="44" height="44" viewBox="0 0 44 44" fill="none" stroke="#fff" stroke-width="2"><path d="M13 15h18v11H20l-5 4v-4h-2z"/></svg></div>

<section class="touch">
  <h2>Let's keep In Touch</h2>
  <div class="form"><div class="field inline">Enter Your Email</div><div class="submit inline">SUBSCRIBE</div></div>
</section>

<footer class="site-footer">
  <div class="col" style="left:100px"><h4>Quick Links</h4><ul class="links-2"><li>Home</li><li>About</li><li>Subscribe</li><li>How To Order</li><li>Our Products</li><li>FAQ</li><li>Blog</li><li>Contact</li></ul></div>
  <div class="col" style="left:400px"><h4>My Account</h4><ul><li>Privacy Policy</li><li>Shipping Policy</li><li>Refund Policy</li><li>Terms &amp; Conditions</li></ul></div>
  <div class="col" style="left:640px"><h4>Contact Detail</h4><ul><li>2210 Meadow Lane, Tulsa OK</li><li>(405) 555-0148</li><li>hello@vivrathc.example</li></ul></div>
  <div class="foot-brand">Vivra THC</div>
  <div class="socials"><div class="inline"></div><span></span><span></span><span></span><span></span></div>
  <div class="copyright">© 2021 Vivra THC. All Rights Reserved.</div>
  <div class="cards" aria-label="Accepted payment cards"><span></span><span></span><span></span><span></span><span></span></div>
  <div class="disclaimer"><h4>Disclaimer</h4><p>Sed ut perspiciatis unde omnis iste natus error sit voluptatem accusantium doloremque laudantium, totam rem aperiam, eaque ipsa quae ab illo inventore veritatis et quasi architecto beatae vitae dicta sunt explicabo. Nemo enim ipsam voluptatem quia voluptas sit aspernatur aut odit aut fugit, sed quia consequuntur magni dolores eos qui ratione voluptatem sequi nesciunt. Neque porro quisquam est, qui dolorem ipsum quia dolor sit amet, consectetur, adipisci velit, sed quia non numquam eius modi tempora incidunt ut labore et dolore magnam aliquam quaerat voluptatem. Ut enim ad minima veniam, quis nostrum exercitationem ullam.</p></div>
</footer>

</body>
</html>
```